Book Cover Design Project For New Nonfiction book

I need a cover designed for a new book/eBook - Little Hands Handbook to Lightening Your Household’s Energy Trail by Maren Holcott.
Below is a description of the book. I don't have a specific idea or vision in mind for the cover. I'd like to see what designs and ideas SketchHive designers come up with.
However, the design needs to work and be effective at both a large book cover size and a small thumbnail-sized image - the way that many people browse book covers on Bookvale and other websites. Therefore, a design that relies on really small details probably won't translate at the smaller image sizes that book covers are displayed online. Just keep that in mind!
Little Hands Handbook to Lightening Your Household’s Energy Trail by Maren Holcott will help you and your family make your way of life greener: by wasting less, reusing and recycling more. Step-by-step, Maren Holcott will show you how you can:
• LIVE a much greener lifestyle without sacrificing much in the way of convenience or time
• HARNESS your children’s natural concern about people and the planet
• EMPOWER your children by helping them improve the world
• SAVE your family gobs of money!
• TRACK your progress with a table at the back of the book, to see how much electricity, water, heat, and cash you save!
Following even just a few of the 102 tips in this ebook can have a big impact on your family's economic savings - and the planet!
Target Market(s)
The book is designed to be read by parents and child
Industry/Entity Type
Recycling
Look and feel

```html
<!DOCTYPE html>
<html lang="en">
<head>
<meta charset="utf-8">
<title>Little Hands Handbook to Lightening Your Household’s Energy Trail — Maren Holcott</title>
<link rel="stylesheet" href="https://fonts.googleapis.com/css2?family=Jost:wght@300&display=swap">
<style>
  :root {
    --page: #ffffff;
    --cover: #ffffff;
    --cover-edge: #3a3a3a;
    --cover-shadow: rgba(0, 0, 0, 0.45);
    --author-grey: #8c8c8c;
    --title-ink: #1c1c1c;
    --leaf-green: #9bc83f;
    --leaf-green-deep: #86b431;
  }
  html, body {
    margin: 0;
    padding: 0;
    width: 872px;
    height: 1200px;
    overflow: hidden;
    background: var(--page);
  }
  .canvas {
    position: relative;
    width: 872px;
    height: 1200px;
  }
  .book-cover {
    position: absolute;
    left: 118px;
    top: 110px;
    width: 630px;
    height: 974px;
    background: var(--cover);
    border: 1px solid var(--cover-edge);
    box-shadow: 5px 5px 6px var(--cover-shadow);
    font-family: "Jost", "Futura", sans-serif;
    font-weight: 300;
    text-align: center;
  }
  .author {
    position: absolute;
    top: 26px;
    left: 0;
    right: 0;
    margin: 0;
    font-size: 62px;
    font-weight: 300;
    letter-spacing: 10px;
    color: var(--author-grey);
    line-height: 1;
  }
  .title {
    position: absolute;
    top: 166px;
    left: 0;
    right: 0;
    margin: 0;
    font-size: 50px;
    font-weight: 300;
    letter-spacing: 2px;
    line-height: 58px;
    color: var(--title-ink);
    text-transform: uppercase;
  }
  .title span { display: block; }
  .footprint-art {
    position: absolute;
    left: 218px;
    top: 530px;
    width: 190px;
    height: 368px;
    border-radius: 95px 95px 80px 80px;
    background: linear-gradient(160deg, var(--leaf-green), var(--leaf-green-deep));
    box-shadow: inset 4px 6px 8px rgba(0, 0, 0, 0.25), 0 0 0 8px #f4f4f4;
  }
</style>
</head>
<body>
  <main class="canvas">
    <section class="book-cover">
      <p class="author">MAREN HOLCOTT</p>
      <h1 class="title">
        <span>Little Hands</span>
        <span>Handbook to</span>
        <span>Lightening Your</span>
        <span>Household’s</span>
        <span>Energy Trail</span>
      </h1>
      <div class="footprint-art" role="img" aria-label="Green footprint pressed into the white cover as a cut-out"></div>
    </section>
  </main>
</body>
</html>
```